massage therapy Business Card Design

massage therapy business card
I would like a custom logo created as well.
My vision is angel wings with the WB business initials in between them.
A very simple design.
Colors preferred are light blues and greens.

Target Market(s)

Massage, Spa, fitness

Industry/Entity Type

Massage Therapy

Contact Information for Business Card

A Willow Breeze
Mara Quint
Massage Therapist and Flowing Pulse Method Practitioner
2718 Bramblewood Lane, Conway, AR 72034
501-384-6190
mara.willowbreeze@mailnest.example

Colors
abd036
33a6d7
3176b5
0255a3
0392cd
9bcb3c
cadf82

Requirements
Must have
• the logo must have angel wing.

```html
<!DOCTYPE html>
<html lang="en">
<head>
<meta charset="utf-8">
<title>A Willow Breeze – Business Card</title>
<link rel="stylesheet" href="https://fonts.googleapis.com/css2?family=Cherry+Swash:wght@700&family=Exo+2:wght@500&family=Open+Sans:wght@400&family=Courgette&family=Arimo&display=swap">
<style>
  :root {
    --card-border: #ffffff;
    --card-sky: #4dd0f4;
    --brand-lime: #a6ec1c;
    --name-blue: #0a4be6;
    --text-white: #ffffff;
    --text-ink: #0c0c0c;
    --wing-light: #f4f9ff;
    --wing-shadow: #cfe3fb;
  }
  html, body {
    margin: 0;
    padding: 0;
    width: 1200px;
    height: 702px;
    overflow: hidden;
    background: var(--card-border);
  }
  .card {
    position: relative;
    width: 1200px;
    height: 702px;
    box-sizing: border-box;
    border: 13px solid var(--card-border);
    background: var(--card-sky);
    overflow: hidden;
  }
  .wing-mark {
    position: absolute;
    left: 51px;
    top: 164px;
    width: 555px;
    height: 305px;
    border-radius: 40% 40% 12% 12%;
    background: radial-gradient(ellipse at 50% 45%, var(--wing-light) 0%, var(--wing-shadow) 55%, rgba(207,227,251,0) 78%);
  }
  .details {
    position: absolute;
    left: 641px;
    top: 0;
    right: 0;
  }
  .brand-name {
    position: absolute;
    top: 124px;
    margin: 0;
    font-family: "Cherry Swash", cursive;
    font-weight: 700;
    font-size: 40px;
    line-height: 52px;
    color: var(--brand-lime);
    white-space: nowrap;
  }
  .person-name {
    position: absolute;
    top: 202px;
    margin: 0;
    font-family: "Exo 2", sans-serif;
    font-weight: 500;
    font-size: 33px;
    line-height: 42px;
    color: var(--name-blue);
    white-space: nowrap;
  }
  .role {
    position: absolute;
    top: 249px;
    margin: 0;
    font-family: "Open Sans", sans-serif;
    font-weight: 400;
    font-size: 25px;
    line-height: 36px;
    color: var(--text-white);
    white-space: nowrap;
  }
  .email {
    position: absolute;
    top: 416px;
    margin: 0;
    font-family: "Courgette", cursive;
    font-size: 28px;
    line-height: 44px;
    color: var(--text-ink);
    white-space: nowrap;
  }
  .address {
    position: absolute;
    top: 573px;
    margin: 0;
    font-family: "Arimo", sans-serif;
    font-style: normal;
    font-size: 24px;
    line-height: 34px;
    color: var(--text-ink);
    white-space: nowrap;
  }
</style>
</head>
<body>
  <main class="card">
    <div class="wing-mark" role="img" aria-label="Logo area: pair of white angel wings with a glowing halo between them"></div>
    <section class="details">
      <h1 class="brand-name">A Willow Breeze</h1>
      <h2 class="person-name">Mara Quint</h2>
      <p class="role">Massage Therapist and<br>Flowing Pulse Method Practitioner</p>
      <p class="email">mara.willowbreeze@mailnest.example</p>
      <address class="address">2718 Bramblewood Lane, Conway, AR 72034<br>501-384-6190</address>
    </section>
  </main>
</body>
</html>
```